Wine Label for my husband’s 50th birthday party

I need a wine label to celebrate my husband’s 50th birthday. We are having a large party for approx 100 guests. My husband is a very proud Wine Grape Grower in The Riverland, South Australia and one of the wineries he supplies has made these wines for him, especially to be consumed at the party - so maybe that they are his grapes can be included in/on the label? His name is Walter, so maybe incorporate that into the label - Walter’s Harvest? The Walter, Exclusive and Limited Release? Label might include his year of birth 1968, eg good year?
There will be various varieties of wine, I will update with the details as soon as I get them. So we may actually need more than 1 label....
The date of the party is 5th May 2018.
My hubby is Greek, is a Greek theme, or Greek gods, Greek mythology might be included?
The photo uploads below are some that I like and that catch my eye.

Target Market(s)

45-55yo

Colors

Designer to choose colors to be used in the design.

Requirements
Must have
• I love some of the quirky wine labels now! Must include my husband’s name, Walter. Perhaps year of birth 1968. Greek theme, mythology, gods etc
Nice to have
• Bright pops of colour. Maybe a Greek theme, perhaps using the variety and Greek god name or theme - Eg Spartan’s Shiraz, Medusa Merlot etc
Should not have
• Grapes, vines, boring colours.

```html
<!DOCTYPE html>
<html lang="en">
<head>
<meta charset="utf-8">
<title>Walter’s Harvest – Cabernet Sauvignon Label</title>
<link href="https://fonts.googleapis.com/css2?family=Playfair+Display:wght@700&family=Source+Serif+4:wght@400;600;700&display=swap" rel="stylesheet">
<style>
  :root {
    --page: #ffffff;
    --label-light: #f1ede4;
    --label-mid: #e6e1d0;
    --label-dark: #d8d3c3;
    --wine-red: #b71c2c;
    --navy: #2a2f45;
    --bronze: #6b4226;
    --coin-fill: #e4dac6;
    --coin-edge: #6b4226;
  }
  * { box-sizing: border-box; margin: 0; padding: 0; }
  html, body {
    width: 1200px;
    height: 1200px;
    overflow: hidden;
    background: var(--page);
  }
  .canvas {
    position: relative;
    width: 1200px;
    height: 1200px;
  }
  .label {
    position: absolute;
    left: 286px;
    top: 245px;
    width: 630px;
    height: 707px;
    background: linear-gradient(100deg, var(--label-light) 0%, var(--label-mid) 35%, var(--label-light) 60%, var(--label-dark) 85%, var(--label-light) 100%);
    box-shadow: 0 4px 12px rgba(0, 0, 0, 0.18);
    font-family: "Source Serif 4", Georgia, serif;
  }
  .coin-art {
    position: absolute;
    left: 112px;
    top: 73px;
    width: 280px;
    height: 280px;
  }
  .vintage-stamp {
    position: absolute;
    left: 361px;
    top: 259px;
    width: 166px;
    height: 98px;
    border: 2px solid var(--wine-red);
    transform: rotate(-4deg);
    text-align: center;
    background: rgba(241, 237, 228, 0.6);
  }
  .vintage-year {
    display: block;
    font-family: "Playfair Display", Georgia, serif;
    font-weight: 700;
    font-size: 49px;
    line-height: 1;
    color: var(--wine-red);
    margin-top: 12px;
  }
  .vintage-note {
    display: block;
    font-weight: 600;
    font-size: 15px;
    color: var(--navy);
    margin-top: 4px;
  }
  .wine-name {
    position: absolute;
    left: 112px;
    top: 360px;
    font-family: "Playfair Display", Georgia, serif;
    font-weight: 700;
    font-size: 88px;
    line-height: 85px;
    letter-spacing: -1px;
    color: var(--wine-red);
    white-space: nowrap;
  }
  .bottle-facts {
    position: absolute;
    left: 113px;
    top: 615px;
    font-size: 15px;
    line-height: 21px;
    color: var(--bronze);
  }
  .variety {
    position: absolute;
    right: 108px;
    top: 620px;
    font-weight: 700;
    font-size: 22px;
    color: var(--bronze);
    letter-spacing: 0.3px;
  }
</style>
</head>
<body>
<div class="canvas">
  <section class="label">
    <svg class="coin-art" viewBox="0 0 280 280" role="img" aria-label="Engraved ancient Greek coin bearing a laurel-crowned bearded god in profile">
      <circle cx="140" cy="140" r="136" fill="var(--coin-fill)" stroke="var(--coin-edge)" stroke-width="3"/>
    </svg>

    <div class="vintage-stamp">
      <span class="vintage-year">1968</span>
      <span class="vintage-note">Limited Release</span>
    </div>

    <h1 class="wine-name">WALTER’S<br>HARVEST</h1>

    <p class="bottle-facts">750 ml<br>alc 13.0% vol</p>
    <p class="variety">Cabernet Sauvignon</p>
  </section>
</div>
</body>
</html>
```